Harrow Glen Kentucky Bourbon Whiskey

We need a label design for a bottle of whiskey. It is for a 750 ml bottle and needs to have a place to write in proof, age, and bottle number at bottom of label. It is a single barrel bourbon. We want to include our tree logo attached in the upload files in some way. Leave out the Distillery part to where it just says Harrow Glen Bourbon Whiskey with the tree. We need the label to be clean and modern. I have also attached a picture of the bottle the label is intended to go on.

Industry/Entity Type

Bourbon

Requirements
Must have
• Harrow Glen tree from file

```html
<!DOCTYPE html>
<html lang="en">
<head>
<meta charset="utf-8">
<title>Harrow Glen Kentucky Bourbon Whiskey — Label</title>
<link rel="stylesheet" href="https://fonts.googleapis.com/css2?family=Alfa+Slab+One&family=Cinzel:wght@500&family=Comfortaa:wght@600&family=Nunito:wght@600;700&display=swap">
<style>
  :root {
    --backdrop: #2a2521;
    --label-black: #1d1d1d;
    --label-gold: #dba634;
    --ink-white: #f4f1ea;
    --ink-gold: #c9922a;
    --ink-dark: #1a1a1a;
  }
  * { margin: 0; padding: 0; box-sizing: border-box; }
  html, body {
    width: 1200px; height: 1200px; overflow: hidden;
    background: var(--backdrop);
  }
  .canvas { position: relative; width: 1200px; height: 1200px; }
  .label {
    position: absolute; left: 280px; top: 60px;
    width: 640px; height: 1080px;
    background: var(--label-black);
    overflow: hidden;
  }
  .brand {
    position: absolute; left: 0; top: 0; width: 100%; height: 295px;
    display: flex; flex-direction: column; align-items: center;
  }
  .brand-mark {
    margin-top: 58px; width: 90px; height: 90px;
    border-radius: 50%; background: var(--ink-gold);
  }
  .brand-name {
    margin-top: 26px;
    font-family: "Cinzel", serif; font-weight: 500;
    font-size: 46px; letter-spacing: 2px;
    color: var(--ink-white);
  }
  .ornament {
    position: absolute; width: 90px; height: 40px;
    border-radius: 20px; background: var(--ink-gold); opacity: .55;
  }
  .ornament.top-left { left: 108px; top: 258px; }
  .ornament.top-right { left: 442px; top: 258px; }
  .ornament.bottom-mid { left: 260px; top: 796px; width: 120px; height: 32px; border-radius: 16px; }
  .gold-band {
    position: absolute; left: 0; top: 305px; width: 100%; height: 480px;
    background: var(--label-gold);
  }
  .style-name {
    position: absolute; left: 138px; top: 545px;
    width: 456px; height: 52px;
    transform: translate(-50%, -50%) rotate(-90deg);
    text-align: center;
    font-family: "Comfortaa", sans-serif; font-weight: 600;
    font-size: 40px; line-height: 52px;
    color: var(--ink-dark);
    white-space: nowrap;
  }
  .product-name {
    position: absolute; left: 187px; top: 318px;
    font-family: "Alfa Slab One", serif; font-weight: 400;
    font-size: 178px; line-height: 152px;
    color: var(--ink-white);
    letter-spacing: -2px;
  }
  .volume {
    position: absolute; left: 0; top: 850px; width: 100%;
    text-align: center;
    font-family: "Nunito", sans-serif; font-weight: 600;
    font-size: 40px; line-height: 48px; color: var(--ink-white);
  }
  .bottle-details {
    position: absolute; left: 60px; right: 60px; top: 940px;
    display: flex; justify-content: space-between; gap: 28px;
    list-style: none;
  }
  .detail-field {
    flex: 1;
    display: flex; flex-direction: column; align-items: center;
  }
  .detail-name {
    font-family: "Nunito", sans-serif; font-weight: 700;
    font-size: 20px; letter-spacing: 3px; text-transform: uppercase;
    color: var(--ink-gold);
  }
  .detail-line {
    margin-top: 40px; width: 100%; height: 2px;
    background: var(--ink-gold); opacity: .8;
  }
</style>
</head>
<body>
<main class="canvas">
  <section class="label" aria-label="Harrow Glen Kentucky Bourbon Whiskey label">
    <header class="brand">
      <div class="brand-mark"></div>
      <p class="brand-name">HARROW GLEN</p>
    </header>
    <div class="gold-band"></div>
    <div class="ornament top-left" role="img" aria-label="Gold scroll ornament"></div>
    <div class="ornament top-right" role="img" aria-label="Gold scroll ornament"></div>
    <div class="style-name">Kentucky Bourbon</div>
    <h1 class="product-name">WH<br>ISK<br>EY</h1>
    <div class="ornament bottom-mid" role="img" aria-label="Gold scroll ornament"></div>
    <p class="volume">750 ml</p>
    <ul class="bottle-details" aria-label="Fields to write in by hand">
      <li class="detail-field"><span class="detail-name">Proof</span><span class="detail-line"></span></li>
      <li class="detail-field"><span class="detail-name">Age</span><span class="detail-line"></span></li>
      <li class="detail-field"><span class="detail-name">Bottle No.</span><span class="detail-line"></span></li>
    </ul>
  </section>
</main>
</body>
</html>
```